2 x Digitize Logo | 2 x Business Cards | 2 x Fridge Magnets

We require 6 deliverables:
1. Residential logo redrawn (same just high quality for large print format).
2. Corporate logo redrawn (minor changes to wording and high quality for large print format).
3. New business card design for Furniture Removals (residential)
4. New business card design for Corporate Relocations (business)
5. New Fridge magnet for Furniture removals (residential)
6. New fridge magnet for Corporate Relocations (business)
1. Residential Logo
a. We require the logo to be translated into a high quality digital image with no modifications.
(see attached resilogo.jpg)
2. Residential Logo
a. We require the logo to be edited (add the word corporate relocations) be translated into a high quality digital image.
(see attached corplogo.jpg)
3. Using the resilogo please make a new business card for our business.
a. Please see the web site https://www.bluegatehaulage.com.au for colours and inspiration.
b. The residential business card needs the following information:
i. Business Name (using the residential logo).
ii. Free Call: 1800 BG Haul (the B, G and Haul much be the same colour as the logo).
iii. Website: www.BluegateHaulage.com.au
iv. Address: 4/6 Marlow Court, VIC 3201
v. Email: move@BluegateHaulage.com.au
vi. backof Card:
Review our service
www.TellTallyHub.com.au
Services: Local, Country, Interstate | Furniture Removals | Piano, Billiard Tables & Antiques
4. Using the corplogo please make a new business card for our business.
b. The corporate business card needs the following information:
i. Business Name (using the corporate logo).
v. Email: corporate@BluegateHaulage.com.au
vi. Back of Card:
Review our service
www.TellTallyHub.com.au
Services: Corporate relocations | Office equipment moves | Packing Service | Packing Materials
5. Using the resilogo please make a new fridge magent for our business.
b. The residential fidge magnet needs the following information:
iv. Services: Local, Country, Interstate | Furniture Removals | Piano, Billiard Tables & Antiques
6. Using the corplogo please make a new fridge magent for our business.
b. The corporate fidge magnet needs the following information:
iv. Services: Local, Country, Interstate | Corporate relocations
Target Market(s)
Residential Furniture Removals and Corporate Office relocations
Industry/Entity Type
Business
Contact Information for Business Card
Please see full brief for six items required
Requirements
Must have
- Clean simple, easy to read
Nice to have
- fresh, stand out, eye catching
Should not have
- plain, standard, boring, general

```html
<!DOCTYPE html>
<html lang="en">
<head>
<meta charset="utf-8">
<title>Bluegate Haulage – Business Card</title>
<link rel="stylesheet" href="https://fonts.googleapis.com/css2?family=Work+Sans:wght@400;500;600;700;800&display=swap">
<style>
  :root {
    --bg: #d9d9d9;
    --card: #ffffff;
    --ink: #5a5a5a;
    --ink-soft: #6e6e6e;
    --red: #e3221c;
    --green: #2eaa3f;
    --yellow: #f4c20d;
    --shadow: rgba(0,0,0,0.18);
  }
  * { box-sizing: border-box; margin: 0; padding: 0; }
  html, body { width: 1200px; height: 900px; overflow: hidden; }
  body {
    background: var(--bg);
    font-family: "Work Sans", Arial, sans-serif;
    color: var(--ink);
    display: flex;
    flex-direction: column;
    align-items: center;
    justify-content: center;
    gap: 40px;
  }
  .card {
    position: relative;
    width: 640px;
    height: 390px;
    background: var(--card);
    box-shadow: 0 8px 24px var(--shadow);
  }

  /* Back side */
  .card-back {
    display: flex;
    flex-direction: column;
    align-items: center;
    text-align: center;
    padding: 26px 48px 0;
  }
  .services-title {
    color: var(--red);
    font-weight: 800;
    font-size: 20px;
    margin-bottom: 4px;
  }
  .services-list {
    font-size: 15px;
    font-weight: 500;
    color: var(--ink-soft);
    line-height: 1.35;
    margin-bottom: 12px;
  }
  .reviewer {
    display: inline-block;
    background: var(--green);
    color: #fff;
    font-weight: 600;
    font-size: 14px;
    padding: 3px 0;
    width: 190px;
    border-radius: 12px;
    margin-bottom: 10px;
  }
  .review {
    font-size: 12.5px;
    line-height: 1.45;
    color: var(--ink);
    margin-bottom: 16px;
  }

  /* Front side */
  .brand {
    position: absolute;
    left: 34px;
    top: 168px;
    display: flex;
    align-items: center;
    gap: 8px;
  }
  .brand-dot {
    width: 14px; height: 14px;
    border-radius: 50%;
    background: var(--green);
  }
  .brand-name {
    font-weight: 800;
    font-size: 26px;
    color: var(--green);
    letter-spacing: 0.2px;
  }
  .divider {
    position: absolute;
    left: 318px;
    top: 148px;
    width: 2px;
    height: 72px;
    background: var(--red);
  }
  .contacts {
    position: absolute;
    left: 338px;
    top: 150px;
    list-style: none;
    font-size: 15.5px;
    color: var(--ink);
    line-height: 1.55;
  }
  .contacts li { display: flex; align-items: center; gap: 12px; }
  .contacts svg { width: 15px; height: 15px; flex: none; }
  .haul-code { font-weight: 800; font-size: 14px; margin-left: 6px; }
  .haul-code .b { color: var(--yellow); }
  .haul-code .g { color: var(--red); }
  .haul-code .h { color: var(--green); }
  .address {
    position: absolute;
    left: 190px;
    bottom: 44px;
    font-size: 16px;
    color: var(--ink);
  }
  .address-label { color: var(--red); }
</style>
</head>
<body>

<section class="card card-back" aria-label="Card back">
  <h2 class="services-title">Service</h2>
  <p class="services-list">Local | Country | Interstate | Furniture<br>Removals | Piano | Billiard Tables &amp; Antiques</p>

  <span class="reviewer">Marcus</span>
  <p class="review">Well, what can I say? Booking process was easy, information clear and concise. Truck turned up exactly on time. Tom and Rhys the right combination of friendly yet professional. Quick and efficient service, very careful with everything, no damage at all. Pricing was very acceptable.</p>

  <span class="reviewer">Gavin And Mel</span>
  <p class="review">Dale and Rhys delivered our new sideboard today, we would like to compliment the company for the efficient, friendly service these two gave us. On the basis of this experience we will not hesitate to use and recommend your company in the future. In short, your refrigerator magnet had gone straight to the pool room!! Thanks from two more satisfied customers.</p>
</section>

<section class="card card-front" aria-label="Card front">
  <div class="brand">
    <span class="brand-dot"></span>
    <span class="brand-name">Bluegate Haulage</span>
  </div>
  <div class="divider"></div>
  <ul class="contacts">
    <li>
      <svg viewBox="0 0 16 16" aria-hidden="true"><path d="M4 1.5l2.2 3-1.3 1.4c.8 1.8 2.4 3.4 4.2 4.2l1.4-1.3 3 2.2-1.3 2.4C7.5 13.2 2.8 8.5 1.6 3z" fill="var(--green)"/></svg>
      <span>Free Call: 1800 <span class="haul-code"><span class="b">B</span> <span class="g">G</span> <span class="h">HAUL</span></span></span>
    </li>
    <li>
      <svg viewBox="0 0 16 16" aria-hidden="true"><rect x="1" y="3.5" width="14" height="9" fill="var(--green)"/><path d="M1.5 4l6.5 5 6.5-5" fill="none" stroke="#fff" stroke-width="1.3"/></svg>
      <span>move@BluegateHaulage.com.au</span>
    </li>
    <li>
      <svg viewBox="0 0 16 16" aria-hidden="true"><g fill="none" stroke="var(--green)" stroke-width="1.4"><circle cx="8" cy="8" r="6.5"/><ellipse cx="8" cy="8" rx="2.8" ry="6.5"/><path d="M1.5 8h13M2.6 4.6h10.8M2.6 11.4h10.8"/></g></svg>
      <span>www.BluegateHaulage.com.au</span>
    </li>
  </ul>
  <p class="address"><span class="address-label">Address:</span> 4/6 Marlow Court, VIC 3201</p>
</section>

</body>
</html>
```